Web Design / Transformation our Joomla web site

Job Type
We are looking for a fresh eye-catching Custom Joomla Design to transform our Joomla web site

Task Description
We are in a process to create web site to Speech Pathology services . The site is built by using brightframe ((http://www.brightframe-example.com/) horizon template.

You can see our site http://pebblelanetherapy-example.com/demo

Unfortunately, this template does not match our identity. We would like to improve or replace it. Although we like features that brightframe template is giving as part of their template ,we want to transform our site to something more simplistic and kids oriented . We don’t like look and fill of our website since it’s very professional and “corporate” . Our business is very small and is not 100 people company , we are looking for something more simple and personal. It should look professional, all be it, child friendly. We work on children’s communication skills, and we want to convey an idea that communication is “Pebble Lane”, meaning children need to learn to play and socialize appropriately. In addition, learning to be a better communicators will help them to be closer to their family members and friends. We want our website to show kids playing and having fun. In other hand , we don't want the Website to be too busy with images, so use your professional judgment.
You can change current template or you can provide your own Joomla design.

Examples of website look that we like :

http://sunnygablestherapy-example.com
http://thetalkinggardeners-example.com/
http://rowanvoiceclinic-example.com/

About Our Company :
Company name: Pebble Lane
What we do: Pediatric Speech & Language Pathology Services. We established Pebble Lane to provide families with a unique option for their child’s speech therapy needs. Our clinic is founded on the principle that all children are different and require a thoughtful, parent-driven therapy plan. When a family chooses us, they will enter a partnership with an experienced, well-trained therapist.
Top Three Things to Communicate through our Website:
#1 - We are kids friendly
#2 - We are professional
#3 - We provide our services with a loving, nurturing attitude toward the child and with compassionate, comprehensive support and input for the family
Updates

To see current running site : http://pebblelanetherapy-example.com/demo/

Reason: There are no good designs to address our needs

Reason: It's still work in progress. Submitted designs are still under constructions and waiting for updates

We are accepting WordPress designs as well !!!

Target Market(s)

Families with kids

Industry/Entity Type

Communication

Requirements
Must have
• • Joomla/Wordpress as a platform
• Easy to Navigate
• Clean Design, kids friendly but professional

```html
<!DOCTYPE html>
<html lang="en">
<head>
<meta charset="utf-8">
<title>Pebble Lane</title>
<link rel="stylesheet" href="https://fonts.googleapis.com/css2?family=Open+Sans:wght@400;600;700&display=swap">
<style>
:root{
  --sky-top:#74c6ee;
  --sky-mid:#bfe4f4;
  --sky-bottom:#f4f4dc;
  --title:#1e7f96;
  --ink:#2b2b2b;
  --frame:#4a4239;
  --white:#ffffff;
  --panel:#e4f3fb;
  --panel-border:#b9dff2;
  --blue-top:#7fd0f5;
  --blue-bottom:#3ea9e0;
  --navy:#1b3550;
  --link:#2a8fd0;
  --rule:#c9c2b5;
  --muted:#5c5348;
  --green-top:#7cc64f;
  --green-bottom:#5aa83a;
  --pencil-top:#f8bd45;
  --pencil-bottom:#f29f22;
  --book-top:#e6dccd;
  --book-bottom:#cdbda5;
  --kids-left:#f3a25a;
  --kids-right:#6cc0e6;
  --orange-top:#ffa53b;
  --orange-bottom:#f07f12;
  --tangerine-top:#ff8a3d;
  --tangerine-bottom:#ec5a10;
  --pink-top:#ef5f9f;
  --pink-bottom:#d9237a;
  --rss:#f6901e;
}
*{box-sizing:border-box;margin:0;padding:0}
html,body{width:1200px;height:900px;overflow:hidden}
body{
  position:relative;
  font-family:"Open Sans",Arial,sans-serif;
  color:var(--ink);
  background:linear-gradient(180deg,var(--sky-top) 0%,var(--sky-mid) 45%,var(--sky-bottom) 85%);
}
.abs{position:absolute}
.tree-art{left:150px;top:0;width:248px;height:150px;border-radius:0 0 8px 8px;
  background:linear-gradient(180deg,var(--green-top),var(--green-bottom))}
.pencil-art{left:867px;top:0;width:255px;height:150px;border-radius:0 0 8px 8px;
  background:linear-gradient(180deg,var(--pencil-top),var(--pencil-bottom))}
.site-title{left:0;width:1150px;top:34px;text-align:center;font-size:30px;font-weight:600;color:var(--title);letter-spacing:.5px}
.site-tagline{left:0;width:1150px;top:72px;text-align:center;font-size:17px;font-weight:600;color:var(--navy)}

.page{left:78px;top:153px;width:1044px;height:702px;border-radius:18px;overflow:hidden;background:var(--white)}
.topbar{left:0;top:0;width:1044px;height:44px;background:var(--frame)}
.nav-btn{top:9px;height:27px;border-radius:6px;font-size:14px;font-weight:700;display:flex;align-items:center;justify-content:center}
.nav-home{left:36px;width:81px;background:linear-gradient(var(--blue-top),var(--blue-bottom));color:var(--navy)}
.nav-contacts{left:130px;width:105px;background:linear-gradient(#6b6157,#4f463d);color:var(--white);border:1px solid #7a6f63}
.footer{left:0;top:639px;width:1044px;height:63px;background:var(--frame)}

.side-box{left:12px;width:207px;background:var(--panel);border:1px solid var(--panel-border);border-radius:8px;overflow:hidden}
.side-head{height:33px;background:linear-gradient(var(--blue-top),var(--blue-bottom));font-size:13px;font-weight:700;color:#0f1f2e;padding:7px 12px}
.side-text{font-size:12px;line-height:17px;padding:10px 40px 0 7px;color:#333}
.side-link{font-size:12px;padding:0 7px;color:var(--link)}
.pill{display:flex;align-items:center;justify-content:center;height:27px;border-radius:14px;background:linear-gradient(#a8e3fa,#4bb4e6);font-size:13px;font-weight:700;color:var(--navy);box-shadow:0 1px 2px rgba(0,0,0,.25)}
.rss-frame{left:30px;top:47px;width:147px;height:71px;border:1px solid #b8c6ce;background:#eef6fa}
.rss-frame span{position:absolute;left:66px;top:29px;width:14px;height:13px;background:#5a8fc8;border:1px solid #fff;outline:1px solid #7b9bb7}

.book-art{left:249px;top:78px;width:251px;height:100px;border-radius:6px;background:linear-gradient(180deg,var(--book-top),var(--book-bottom))}
.kids-art{left:544px;top:61px;width:481px;height:241px;border-radius:6px;background:linear-gradient(90deg,var(--kids-left),var(--kids-right))}
.history-title{left:255px;top:215px;font-size:15px;font-weight:700;color:var(--navy);letter-spacing:.3px}
.history-btn{left:242px;top:243px;width:150px}
.rule{left:242px;width:790px;height:2px;background:var(--rule)}
.about-title{left:260px;top:322px;font-size:19px;font-weight:600;color:var(--muted)}
.tile{top:387px;width:172px;height:132px;border-radius:6px;display:flex;align-items:center;justify-content:center;text-align:center;color:var(--white);font-size:18px;font-weight:700;line-height:20px;text-shadow:0 1px 2px rgba(0,0,0,.2)}
.tile-programs{left:262px;background:linear-gradient(var(--orange-top),var(--orange-bottom))}
.tile-teachers{left:522px;background:linear-gradient(var(--tangerine-top),var(--tangerine-bottom))}
.tile-services{left:791px;background:linear-gradient(var(--pink-top),var(--pink-bottom))}
.work-text{left:242px;top:580px;font-size:13px;color:#333}
.work-link{left:242px;top:604px;font-size:13px;color:var(--link)}

.rss-dot{left:24px;top:657px;width:33px;height:27px;border-radius:8px;background:var(--rss)}
.footer-links{left:75px;top:660px;font-size:11px;color:#d8d0c4}
.footer-links a{color:#d8d0c4}
.footer-copy{left:184px;top:672px;font-size:11px;color:#e8e2d8}
</style>
</head>
<body>
  <div class="abs tree-art" role="img" aria-label="Illustration of a green leafy tree"></div>
  <div class="abs pencil-art" role="img" aria-label="Illustration of a stack of yellow pencils"></div>
  <h1 class="abs site-title">Pebble Lane</h1>
  <p class="abs site-tagline">Grow With us</p>

  <div class="abs page">
    <div class="abs topbar"></div>
    <div class="abs nav-btn nav-home">Home</div>
    <div class="abs nav-btn nav-contacts">Contacts</div>

    <div class="abs side-box" style="top:52px;height:105px">
      <div class="side-head">Welcome to our center</div>
      <p class="side-text">Describe here your taglin or Write your message.....</p>
      <p class="side-link">Learn more »</p>
    </div>
    <div class="abs side-box" style="top:167px;height:130px">
      <div class="side-head">RSS</div>
      <div class="abs rss-frame"><span></span></div>
    </div>
    <div class="abs side-box" style="top:307px;height:118px">
      <div class="side-head">Success stories</div>
      <p class="side-text">Write here your success stories .....</p>
      <div class="pill" style="margin:6px 0 0 5px;width:150px">Learn more »</div>
    </div>

    <div class="abs book-art" role="img" aria-label="Photo of an open book with fanned pages"></div>
    <div class="abs kids-art" role="img" aria-label="Photo of a group of children in colourful t-shirts standing together"></div>
    <h2 class="abs history-title">OUR HISTORY</h2>
    <div class="abs pill history-btn">Learn more »</div>

    <div class="abs rule" style="top:305px"></div>
    <h2 class="abs about-title">About Us</h2>
    <div class="abs rule" style="top:361px;height:1px"></div>

    <div class="abs tile tile-programs">OUR<br>PROGRAMS</div>
    <div class="abs tile tile-teachers">OUR<br>TEACHERS</div>
    <div class="abs tile tile-services">OUR<br>SERVICES</div>

    <p class="abs work-text">Describe HERE your work...</p>
    <p class="abs work-link">Learn more »</p>

    <div class="abs footer"></div>
    <div class="abs rss-dot"></div>
    <p class="abs footer-links"><a href="#">Programms</a> | <a href="#">Teachers</a> | <a href="#">Services</a></p>
    <p class="abs footer-copy">All Rights Reserved.</p>
  </div>
</body>
</html>
```